Baked goods front of bag sticker

Pebblecrest Brownies,
2 Go size (clear plastic bag of handful of ¼” square bites)
There will also be larger sizes and custom options(corporate/events) using the same image.
Deliverables Needed:
Need sticker with “Pebblecrest Brownies” for front of bag, approximate 2” circle or rectangle/square.
Packaging front sticker design should be sizable for other media, ie website, future packaging, logo.
Flavor should be indicated on second sticker that integrates well.
Back sticker is already complete and includes ingredients, company name, health dept permit, and other legal necessities. Font will be changed to integrate with front.
Flavors:
1. Sunset Maple Brownie
2. Honeycomb Glow Brownie
3. Zip Zop Mint
4. Crumbly Oat Delight (not so gooey but great)
Primary Audiences:
Anyone who wants a sweet treat to enjoy, and maybe share, on the go. Audience wants a fresh treat with real ingredients they know and love (real butter, Pure vanilla, Fresh eggs)
Audience wants something from a baker not a machine.
Sold at checkout in stores that don’t have baked goods, higher end convenience stores, specialty stores, small gourmet stores, theaters, toy stores, sports arenas, etc.
Will be sampled at events (festivals, movie screenings, races)
Tone and Image:
Fresh, Fun and frank with real ingredients you know
Because it is little and is home-baked, it should be perceived as a little treat without the guilt.
Messages:
Fresh, natural, little treat on the run.
Dear Designers,

```html
<!DOCTYPE html>
<html lang="en">
<head>
<meta charset="utf-8">
<title>Pebblecrest Brownies – Flavour Stickers</title>
<link rel="stylesheet" href="https://fonts.googleapis.com/css2?family=Didact+Gothic&family=Rokkitt:wght@700&display=swap">
<style>
  :root {
    --bg-light: #f4f4f4;
    --bg-dark: #dedede;
    --sage-light: #cfdba6;
    --sage: #b3c383;
    --sage-deep: #a2b46f;
    --cocoa: #5a4232;
    --cream-line: #e6edcc;
    --swirl: rgba(255, 255, 255, 0.18);
  }
  * { margin: 0; padding: 0; box-sizing: border-box; }
  html, body { width: 1200px; height: 849px; overflow: hidden; }
  body {
    position: relative;
    background: radial-gradient(ellipse at 45% 40%, var(--bg-light) 0%, var(--bg-dark) 100%);
    font-family: "Didact Gothic", sans-serif;
    color: var(--cocoa);
  }
  .shape-defs { position: absolute; width: 0; height: 0; }

  .sticker {
    position: absolute;
    width: 296px;
    height: 142px;
  }
  .sticker-shape { position: absolute; inset: 0; width: 100%; height: 100%; }
  .sticker-body { fill: url(#sageFill); stroke: var(--cocoa); stroke-width: 8; }
  .sticker-stitch { fill: none; stroke: var(--cream-line); stroke-width: 1.6; stroke-dasharray: 5 4; }

  .swirl-area {
    position: absolute;
    left: 40%; top: 14%;
    width: 48%; height: 50%;
    border-radius: 50%;
    background: radial-gradient(ellipse, var(--swirl) 0%, rgba(255,255,255,0) 70%);
  }

  .wordmark {
    position: absolute;
    left: 0; right: 0; top: 20px;
    text-align: center;
    line-height: 1;
  }
  .wordmark-name {
    display: block;
    font-size: 36px;
    letter-spacing: 0.5px;
  }
  .wordmark-sub {
    display: block;
    font-size: 15px;
    margin-top: 3px;
    padding-left: 70px;
  }
  .wordmark-dot {
    display: inline-block;
    width: 7px; height: 7px;
    border-radius: 50%;
    background: var(--cocoa);
    margin-left: 4px;
    vertical-align: 6px;
  }
  .flavour {
    position: absolute;
    left: 0; right: 0;
    top: 92px;
    text-align: center;
    font-family: "Rokkitt", serif;
    font-weight: 700;
    font-size: 14px;
    line-height: 1.25;
  }
  .flavour.single { top: 102px; }

  .set-classic .s1 { left: 31px;  top: 31px; }
  .set-classic .s2 { left: 343px; top: 31px; }
  .set-classic .s3 { left: 31px;  top: 246px; }
  .set-classic .s4 { left: 343px; top: 246px; }

  .set-stitched .s1 { left: 574px; top: 420px; }
  .set-stitched .s2 { left: 878px; top: 420px; }
  .set-stitched .s3 { left: 574px; top: 625px; }
  .set-stitched .s4 { left: 878px; top: 625px; }
</style>
</head>
<body>

<svg class="shape-defs" aria-hidden="true">
  <defs>
    <linearGradient id="sageFill" x1="0" y1="0" x2="0" y2="1">
      <stop offset="0" stop-color="#cfdba6"/>
      <stop offset="1" stop-color="#a9ba76"/>
    </linearGradient>
    <path id="cloudOutline" d="M60 12 Q150 -2 240 12 Q262 2 278 18 Q298 34 288 54 Q300 71 288 88 Q298 108 278 124 Q262 140 240 130 Q150 144 60 130 Q38 140 22 124 Q2 108 12 88 Q0 71 12 54 Q2 34 22 18 Q38 2 60 12 Z"/>
  </defs>
</svg>

<section class="sticker-set set-classic">
  <article class="sticker s1">
    <svg class="sticker-shape" viewBox="-6 -4 312 150"><use href="#cloudOutline" class="sticker-body"/></svg>
    <div class="swirl-area" role="img" aria-label="faint floral swirl decoration"></div>
    <h2 class="wordmark"><span class="wordmark-name">Pebblecrest</span><span class="wordmark-sub">Brownies</span></h2>
    <p class="flavour">Sunset Maple<br>Brownie</p>
  </article>
  <article class="sticker s2">
    <svg class="sticker-shape" viewBox="-6 -4 312 150"><use href="#cloudOutline" class="sticker-body"/></svg>
    <div class="swirl-area" role="img" aria-label="faint floral swirl decoration"></div>
    <h2 class="wordmark"><span class="wordmark-name">Pebblecrest</span><span class="wordmark-sub">Brownies</span></h2>
    <p class="flavour">Honeycomb Glow<br>Brownie</p>
  </article>
  <article class="sticker s3">
    <svg class="sticker-shape" viewBox="-6 -4 312 150"><use href="#cloudOutline" class="sticker-body"/></svg>
    <div class="swirl-area" role="img" aria-label="faint floral swirl decoration"></div>
    <h2 class="wordmark"><span class="wordmark-name">Pebblecrest</span><span class="wordmark-sub">Brownies</span></h2>
    <p class="flavour single">Zip Zop Mint</p>
  </article>
  <article class="sticker s4">
    <svg class="sticker-shape" viewBox="-6 -4 312 150"><use href="#cloudOutline" class="sticker-body"/></svg>
    <div class="swirl-area" role="img" aria-label="faint floral swirl decoration"></div>
    <h2 class="wordmark"><span class="wordmark-name">Pebblecrest</span><span class="wordmark-sub">Brownies</span></h2>
    <p class="flavour single">Crumbly Oat Delight</p>
  </article>
</section>

<section class="sticker-set set-stitched">
  <article class="sticker s1">
    <svg class="sticker-shape" viewBox="-6 -4 312 150"><use href="#cloudOutline" class="sticker-body"/><use href="#cloudOutline" class="sticker-stitch" transform="translate(14 9) scale(0.906 0.875)"/></svg>
    <h2 class="wordmark"><span class="wordmark-name">Pebblecrest<span class="wordmark-dot"></span></span><span class="wordmark-sub">Brownies</span></h2>
    <p class="flavour">Sunset Maple<br>Brownie</p>
  </article>
  <article class="sticker s2">
    <svg class="sticker-shape" viewBox="-6 -4 312 150"><use href="#cloudOutline" class="sticker-body"/><use href="#cloudOutline" class="sticker-stitch" transform="translate(14 9) scale(0.906 0.875)"/></svg>
    <h2 class="wordmark"><span class="wordmark-name">Pebblecrest<span class="wordmark-dot"></span></span><span class="wordmark-sub">Brownies</span></h2>
    <p class="flavour">Honeycomb Glow<br>Brownie</p>
  </article>
  <article class="sticker s3">
    <svg class="sticker-shape" viewBox="-6 -4 312 150"><use href="#cloudOutline" class="sticker-body"/><use href="#cloudOutline" class="sticker-stitch" transform="translate(14 9) scale(0.906 0.875)"/></svg>
    <h2 class="wordmark"><span class="wordmark-name">Pebblecrest<span class="wordmark-dot"></span></span><span class="wordmark-sub">Brownies</span></h2>
    <p class="flavour single">Zip Zop Mint</p>
  </article>
  <article class="sticker s4">
    <svg class="sticker-shape" viewBox="-6 -4 312 150"><use href="#cloudOutline" class="sticker-body"/><use href="#cloudOutline" class="sticker-stitch" transform="translate(14 9) scale(0.906 0.875)"/></svg>
    <h2 class="wordmark"><span class="wordmark-name">Pebblecrest<span class="wordmark-dot"></span></span><span class="wordmark-sub">Brownies</span></h2>
    <p class="flavour single">Crumbly Oat Delight</p>
  </article>
</section>

</body>
</html>
```